BrindleStaffing Business Card Design

We are a staffing company finding positions for dedicated nurses and physicians.

Target Market(s)

Business Professionals

Industry/Entity Type

Staffing

Contact Information for Business Card

Gregory Malden
Chairman
417 39th Crescent South
SAINT PETERSBURG FL 33719
813-555-0147 Mobile
813-555-0183 Fax
gmalden@brindlestaffing.example
www.brindlestaffing.example

Font styles to use
Sans Serif

Colors
fbee3e
f04a50
f37122

Requirements
Must have
• Logo Attached, see colors below. We'd like to see Yellow, Orange and Red.

```html
<!DOCTYPE html>
<html lang="en">
<head>
<meta charset="utf-8">
<title>BrindleStaffing Business Card</title>
<link href="https://fonts.googleapis.com/css2?family=Poppins:wght@600&family=Open+Sans:wght@400;600;700&display=swap" rel="stylesheet">
<style>
  :root{
    --backdrop:#6a6a6c;
    --backdrop-edge:#4a494b;
    --card:#ffffff;
    --card-edge:#3d3d3d;
    --red:#f04a50;
    --orange:#f37122;
    --yellow:#fbee3e;
    --ink:#222326;
    --divider:#b9b9b9;
    --panel:#fef7cf;
  }
  *{box-sizing:border-box;margin:0;padding:0}
  html,body{width:1200px;height:1135px;overflow:hidden}
  body{
    position:relative;
    background:radial-gradient(circle at 50% 50%, #929294 0%, var(--backdrop) 45%, var(--backdrop-edge) 100%);
    font-family:"Open Sans", Arial, sans-serif;
  }
  .card{
    position:absolute;
    width:716px;height:408px;
    background:var(--card);
    overflow:hidden;
  }
  .card--front{left:81px;top:115px;border-radius:26px;border:1px solid var(--card-edge)}
  .card--back{left:346px;top:595px;border-radius:42px}

  .brand-name{
    position:absolute;left:0;right:0;text-align:center;
    font-family:"Poppins", Arial, sans-serif;font-weight:600;
    color:var(--red);letter-spacing:-1px;line-height:1;
  }
  .card--front .brand-name{top:72px;font-size:56px}

  .identity{position:absolute;right:388px;top:200px;text-align:right}
  .identity .person{font-weight:700;font-size:33px;color:var(--red);line-height:1;white-space:nowrap}
  .identity .role{font-weight:400;font-size:30px;color:var(--orange);line-height:1;margin-top:10px}
  .divider{position:absolute;left:349px;top:190px;width:1px;height:100px;background:var(--divider)}

  .contacts{position:absolute;left:369px;top:187px;list-style:none}
  .contacts li{display:flex;align-items:center;height:26px;font-size:18px;color:var(--ink);white-space:nowrap}
  .contacts svg{width:17px;height:17px;margin-right:12px;flex:none}
  .contacts .tag{color:var(--orange);font-size:14px;margin-left:8px}

  .address-band{
    position:absolute;left:0;right:0;top:328px;height:46px;
    border-top:1px solid var(--red);border-bottom:1px solid var(--red);
    padding:2px 0;
  }
  .address-band p{
    height:100%;background:var(--orange);color:#fff;
    font-size:18.5px;text-align:center;line-height:39px;
  }

  .back-cross-vertical{position:absolute;left:287px;top:0;width:164px;height:100%;background:var(--panel)}
  .back-panel{position:absolute;left:165px;top:122px;width:409px;height:164px;background:var(--panel)}
  .card--back .brand-name{top:160px;font-size:66px}
  .back-url{
    position:absolute;left:0;right:0;top:246px;text-align:center;
    font-size:21px;letter-spacing:3px;color:var(--ink);
  }
  .back-url .o{color:var(--orange);font-weight:700}
  .back-url .r{color:var(--red);font-weight:700}
</style>
</head>
<body>

<section class="card card--front">
  <div class="brand-name">BrindleStaffing</div>

  <div class="identity">
    <div class="person">Gregory Malden</div>
    <div class="role">Chairman</div>
  </div>
  <div class="divider"></div>

  <ul class="contacts">
    <li>
      <svg viewBox="0 0 20 20"><circle cx="10" cy="10" r="8.5" fill="none" stroke="#f37122" stroke-width="1.5"/><path d="M7 5.5c-1 1.5-.5 5 2 7.5s5 3 6 2l-1.6-1.8-1.4.8c-1-.5-2.5-2-3-3l.8-1.4z" fill="#f37122"/></svg>
      813-555-0147<span class="tag">Mobile</span>
    </li>
    <li>
      <svg viewBox="0 0 20 20"><rect x="5" y="2" width="10" height="6" fill="none" stroke="#f37122" stroke-width="1.4"/><rect x="2" y="8" width="16" height="7" rx="1.5" fill="#f37122"/><rect x="5" y="13" width="10" height="5" fill="#fff" stroke="#f37122" stroke-width="1.4"/></svg>
      813-555-0183<span class="tag">Fax</span>
    </li>
    <li>
      <svg viewBox="0 0 20 20"><path d="M2 8l8-5 8 5v9H2z" fill="#f37122"/><path d="M3 8.5l7 4.5 7-4.5" fill="none" stroke="#fff" stroke-width="1.4"/></svg>
      gmalden@brindlestaffing.example
    </li>
    <li>
      <svg viewBox="0 0 20 20" fill="none" stroke="#f37122" stroke-width="1.2"><circle cx="10" cy="10" r="8"/><ellipse cx="10" cy="10" rx="3.5" ry="8"/><path d="M2 10h16M3.5 6h13M3.5 14h13"/></svg>
      www.brindlestaffing.example
    </li>
  </ul>

  <div class="address-band"><p>417 39th Crescent South, Saint petersburg fl 33719</p></div>
</section>

<section class="card card--back">
  <div class="back-cross-vertical"></div>
  <div class="back-panel"></div>
  <div class="brand-name">BrindleStaffing</div>
  <div class="back-url">www.<span class="o">brindle</span><span class="r">staffing</span>.example</div>
</section>

</body>
</html>
```